Letterhead for new real estate company in South Africa named Lofthaven

A letterhead with the directors and company details to be editable as these changes often

Target Market(s)

In line with our logo brief and our newly designed logo and corporate fee

Industry/Entity Type

Real Estate

Requirements
Must have
• Details as per the sample letterhead provided.

```html
<!DOCTYPE html>
<html lang="en">
<head>
<meta charset="utf-8">
<title>Lofthaven Letterhead</title>
<link href="https://fonts.googleapis.com/css2?family=Libre+Franklin:wght@400;500;700&display=swap" rel="stylesheet">
<style>
  :root {
    --brand-green: #34b27a;
    --brand-brown: #6f6255;
    --accent-red: #d3232b;
    --ink: #1c1c1c;
    --paper: #ffffff;
    --mark-tint: #e6f4ec;
  }
  html, body { margin: 0; padding: 0; overflow: hidden; background: var(--paper); }
  .letterhead {
    position: relative;
    width: 927px;
    height: 1200px;
    overflow: hidden;
    background: var(--paper);
    font-family: "Libre Franklin", Arial, sans-serif;
    color: var(--ink);
  }
  .edge-bands, .corner-bands { position: absolute; display: block; }
  .edge-bands { left: 0; top: 0; width: 28px; height: 1200px; }
  .corner-bands { right: 0; bottom: 0; width: 320px; height: 30px; }

  .brand-name {
    position: absolute;
    left: 62px;
    top: 52px;
    display: flex;
    align-items: center;
    gap: 14px;
    margin: 0;
    font-size: 46px;
    font-weight: 500;
    letter-spacing: -0.5px;
    color: var(--brand-green);
  }
  .brand-dot {
    width: 26px; height: 26px;
    border-radius: 50%;
    background: var(--brand-green);
  }

  .brand-backdrop {
    position: absolute;
    left: 430px;
    top: 465px;
    width: 497px;
    height: 545px;
    background: radial-gradient(ellipse at 55% 45%, var(--mark-tint) 0%, rgba(230,244,236,0.55) 45%, rgba(255,255,255,0) 72%);
  }

  .company-details {
    position: absolute;
    left: 30px;
    top: 1034px;
    font-size: 13.2px;
    line-height: 16.5px;
    margin: 0;
  }
  .company-details p { margin: 0; }
  .company-details .contact-line { margin-top: 6px; }

  .directors {
    position: absolute;
    right: 28px;
    top: 1034px;
    text-align: right;
    font-size: 13.2px;
    line-height: 17.5px;
  }
  .directors-title { margin: 0 0 10px; color: var(--accent-red); font-weight: 700; font-size: 13.2px; }
  .directors-list { margin: 0; padding: 0; list-style: none; font-weight: 700; }
  .franchise-note { margin: 17px 0 0; font-weight: 400; }
</style>
</head>
<body>
<main class="letterhead">
  <svg class="edge-bands" viewBox="0 0 28 1200" aria-hidden="true">
    <rect x="0" y="0" width="15" height="1200" fill="var(--brand-brown)"/>
    <polygon points="15,0 27,0 27,1021 15,1033" fill="var(--brand-green)"/>
  </svg>

  <h1 class="brand-name"><span class="brand-dot"></span>Lofthaven</h1>

  <div class="brand-backdrop" role="img" aria-label="Faint brand emblem decoration"></div>

  <section class="company-details">
    <p>Highveld Realty (Pty) Ltd Va Hearthline Fairmead/Oakridge, Reg No: 2019/458207/07</p>
    <p>Shop G12B, Acacia Crossing, Corner Marula Avenue &amp; Kiepersol Road</p>
    <p>Northwold, South Africa</p>
    <p class="contact-line">Tel: 087 555 0143</p>
    <p class="contact-line">Web: www.hearthline.co.za</p>
  </section>

  <section class="directors">
    <h2 class="directors-title">Directors:</h2>
    <ul class="directors-list">
      <li>K Vermaak</li>
      <li>LP Ashworth-Dlamini</li>
    </ul>
    <p class="franchise-note">Each franchise is independently owned and operated</p>
  </section>

  <svg class="corner-bands" viewBox="0 0 320 30" aria-hidden="true">
    <polygon points="84,3 320,3 320,15 72,15" fill="var(--brand-green)"/>
    <polygon points="30,15 320,15 320,30 15,30" fill="var(--brand-brown)"/>
  </svg>
</main>
</body>
</html>
```